Unique and original Business Card for Financial Services Business

I have moved premises and need to change the detail on my business card so thought now is a good time for a re-design. Looking for something professional and modern with colours to fit in with out logo. Like the idea of foil or embossing if that works but not a must have but I do want something that stands out and that I could not design myself.

Once business card is designed I will also be looking to get letterhead and flyers done but want the business card concept in place first.

The majority of designs I am receiving are generic and template based. I am looking for something unique and original. We have some great design elements in our logo, think outside the box and show me something that stands out from the crowd.

Target Market(s)

Business Professionals

Industry/Entity Type

Finance

Contact Information for Business Card

Name: Delia Norwood Phone 0473 958 162 Address PO Box 8617 Mossvale NSW 2389 Email info@steadyharbourfinancialservices.com.au website www.steadyharbourfinancialservices.com.au

Font styles to use
Other font styles liked:
• Ralway

Requirements
Should not have
• No black backgrounds please

```html
<!DOCTYPE html>
<html lang="en">
<head>
<meta charset="utf-8">
<title>Steady Harbour – Business Card</title>
<link rel="stylesheet" href="https://fonts.googleapis.com/css2?family=Oswald:wght@500&family=Poppins:wght@300;400&display=swap">
<style>
  :root {
    --stage: #d9dcdd;
    --card: #f7f8f8;
    --teal: #00808c;
    --teal-bright: #0f8f9b;
    --ink-dark: #2b3033;
    --ink-grey: #5d6366;
    --rule: #a9aeb0;
  }
  * { box-sizing: border-box; margin: 0; padding: 0; }
  html, body { width: 1200px; height: 900px; overflow: hidden; }
  body {
    background: var(--stage);
    display: flex;
    flex-direction: column;
    align-items: center;
    justify-content: center;
    gap: 44px;
    font-family: "Poppins", sans-serif;
  }
  .card {
    position: relative;
    width: 660px;
    height: 377px;
    background: var(--card);
    box-shadow: 0 8px 24px rgba(0,0,0,.18);
    overflow: hidden;
  }
  .card__band {
    position: absolute;
    left: 0; right: 0; bottom: 0;
    height: 14px;
    background: var(--teal);
  }

  /* Front */
  .brand {
    position: absolute;
    left: 0; right: 0; top: 150px;
    display: flex;
    align-items: center;
    justify-content: center;
    gap: 16px;
  }
  .brand__mark {
    width: 18px; height: 18px;
    background: var(--teal-bright);
  }
  .brand__name {
    font-weight: 300;
    font-size: 46px;
    line-height: 1;
    letter-spacing: 1px;
    color: var(--teal-bright);
    text-transform: uppercase;
  }

  /* Back */
  .person {
    position: absolute;
    left: 60px; top: 118px;
    width: 225px;
  }
  .person__name {
    font-family: "Oswald", sans-serif;
    font-weight: 500;
    font-size: 30px;
    line-height: 1.1;
    text-transform: uppercase;
    white-space: nowrap;
  }
  .person__first { color: var(--teal-bright); }
  .person__last { color: var(--ink-grey); }
  .person__role {
    font-size: 15px;
    color: var(--ink-dark);
    margin-top: 2px;
  }
  .divider {
    position: absolute;
    left: 296px; top: 112px;
    width: 1px; height: 92px;
    background: var(--rule);
  }
  .contact {
    position: absolute;
    left: 316px; top: 116px;
    list-style: none;
    display: flex;
    flex-direction: column;
    gap: 9px;
  }
  .contact__item {
    display: flex;
    align-items: center;
    gap: 8px;
    font-size: 12.5px;
    color: var(--ink-dark);
    white-space: nowrap;
  }
  .contact__icon { width: 15px; height: 15px; flex: none; }
  .address {
    position: absolute;
    left: 0; right: 0; bottom: 46px;
    text-align: center;
    font-size: 16px;
    color: var(--ink-dark);
  }
</style>
</head>
<body>

  <section class="card card--front" aria-label="Card front">
    <div class="brand">
      <span class="brand__mark"></span>
      <span class="brand__name">Steady Harbour</span>
    </div>
    <div class="card__band"></div>
  </section>

  <section class="card card--back" aria-label="Card back">
    <div class="person">
      <p class="person__name"><span class="person__first">Delia</span> <span class="person__last">Norwood</span></p>
      <p class="person__role">Managing Director</p>
    </div>
    <div class="divider"></div>
    <ul class="contact">
      <li class="contact__item">
        <svg class="contact__icon" viewBox="0 0 24 24" aria-hidden="true"><path fill="#0f8f9b" d="M6.6 10.8c1.4 2.8 3.8 5.1 6.6 6.6l2.2-2.2c.3-.3.7-.4 1-.2 1.1.4 2.3.6 3.6.6.6 0 1 .4 1 1V20c0 .6-.4 1-1 1C10.6 21 3 13.4 3 4c0-.6.4-1 1-1h3.5c.6 0 1 .4 1 1 0 1.3.2 2.5.6 3.6.1.3 0 .7-.2 1l-2.3 2.2z"/></svg>
        0473 958 162
      </li>
      <li class="contact__item">
        <svg class="contact__icon" viewBox="0 0 24 24" aria-hidden="true"><rect x="2" y="5" width="20" height="14" fill="none" stroke="#0f8f9b" stroke-width="2"/><path d="M2 5l10 8 10-8" fill="none" stroke="#0f8f9b" stroke-width="2"/></svg>
        info@steadyharbourfinancialservices.com.au
      </li>
      <li class="contact__item">
        <svg class="contact__icon" viewBox="0 0 24 24" aria-hidden="true"><g fill="none" stroke="#0f8f9b" stroke-width="2"><circle cx="12" cy="12" r="9"/><ellipse cx="12" cy="12" rx="4" ry="9"/><path d="M3 12h18M5 7h14M5 17h14"/></g></svg>
        www.steadyharbourfinancialservices.com.au
      </li>
    </ul>
    <p class="address">PO Box 8617 Mossvale NSW 2389</p>
    <div class="card__band"></div>
  </section>

</body>
</html>
```